K Velmor Architectural Construction & Abatement, Inc.
K Velmor Architectural Construction, Inc.
Pilo 47:
86# Has very little orange. Use these colors please. Read all the reviews I gave other designers. Incorporate these ideas into to your design. Push forth these ideas.
Thank you,
rovatique:
Use more green color. Green on back of the card. And on stationary. Continue to push forth with these ideas.
Trulsen:
# 83 Remove the fax information on stationary
# 83 remove the black color on cards & Stationary. Use the original colors. Place motto on back as well.
Use little more green color on front. Green Energy feel. Use the orange as well. Put the logos on envelopes.
erovatique:
Please, include my education on the business cards. BArch, MArch. Thank You.
Pilo47:
Please, find away to include my education details on my business cards: BArch, MArch
I like some of the cards you have put together so far. And I have selected my favorites my star rating system. I asked that the front remain the same. But, the back have another logo which says K Velmor Architect ABATEMENT. I will upload the design for the business cards. Continue, to push the ideas.

```html
<!DOCTYPE html>
<html lang="en">
<head>
<meta charset="utf-8">
<title>K Velmor Architects – Business Card</title>
<link rel="stylesheet" href="https://fonts.googleapis.com/css2?family=Source+Sans+3:wght@400;600;700&display=swap">
<style>
  :root {
    --backdrop: #e9e6e1;
    --card-white: #ffffff;
    --brand-green: #6aa84f;
    --brand-orange: #d9622b;
    --text-light: #ffffff;
  }
  * { margin: 0; padding: 0; box-sizing: border-box; }
  html, body {
    width: 1200px;
    height: 778px;
    overflow: hidden;
    background: var(--backdrop);
    font-family: "Source Sans 3", Arial, sans-serif;
  }
  .card {
    position: absolute;
    left: 168px;
    top: 144px;
    width: 864px;
    height: 492px;
    border-radius: 28px;
    overflow: hidden;
    background: var(--card-white);
    box-shadow: 0 3px 10px rgba(0,0,0,0.12);
  }
  .card__divider {
    position: absolute;
    left: 425px;
    top: 0;
    width: 3px;
    height: 100%;
    background: var(--brand-orange);
  }
  .card__panel {
    position: absolute;
    left: 439px;
    top: 0;
    right: 0;
    height: 100%;
    background: var(--brand-green);
    color: var(--text-light);
  }
  .brand {
    position: absolute;
    left: 60px;
    top: 226px;
    width: 340px;
    height: 48px;
    display: flex;
    align-items: center;
    gap: 14px;
  }
  .brand__square {
    width: 40px;
    height: 40px;
    background: var(--brand-green);
    flex: none;
  }
  .brand__name {
    font-size: 35px;
    font-weight: 700;
    color: var(--brand-green);
    line-height: 1;
    white-space: nowrap;
  }
  .person {
    position: absolute;
    left: 58px;
    top: 126px;
  }
  .person__name {
    font-size: 31px;
    font-weight: 600;
    line-height: 36px;
  }
  .person__title {
    font-size: 21px;
    font-weight: 400;
    line-height: 28px;
    margin-top: 2px;
  }
  .contact {
    position: absolute;
    left: 58px;
    top: 270px;
    font-size: 20px;
    line-height: 33px;
  }
  .contact__address { margin-bottom: 4px; }
  .contact__row {
    display: flex;
    align-items: center;
    gap: 10px;
  }
  .contact__icon { width: 14px; height: 14px; flex: none; }
</style>
</head>
<body>
  <div class="card">
    <div class="brand">
      <span class="brand__square"></span>
      <span class="brand__name">K Velmor Architects</span>
    </div>

    <div class="card__divider"></div>

    <div class="card__panel">
      <div class="person">
        <div class="person__name">Marlon Reyes</div>
        <div class="person__title">Architect Intern / Project Manager</div>
      </div>

      <div class="contact">
        <div class="contact__address">
          5203 FM 2290 North<br>
          Caldwell, Texas 77836
        </div>
        <div class="contact__row">
          <svg class="contact__icon" viewBox="0 0 14 14" aria-hidden="true">
            <rect x="3.5" y="0.5" width="7" height="13" rx="1.5" fill="none" stroke="#fff" stroke-width="1.4"/>
            <rect x="5" y="2.5" width="4" height="6" fill="#fff"/>
          </svg>
          <span>(555) 318-2704</span>
        </div>
        <div class="contact__row">
          <svg class="contact__icon" viewBox="0 0 14 14" aria-hidden="true">
            <rect x="0.7" y="2.5" width="12.6" height="9" fill="none" stroke="#fff" stroke-width="1.4"/>
            <path d="M0.7 2.5 L7 8 L13.3 2.5" fill="none" stroke="#fff" stroke-width="1.4"/>
          </svg>
          <span>kvelmorconstr@mailbox.example</span>
        </div>
      </div>
    </div>
  </div>
</body>
</html>
```